Business Card design for Accounting and Consulting Firm
R.T. BALLISTER HOLDINGS, LLC
Business Card design for Accounting and Consulting Firm - Financial Services
Creative Brief
Use same font as used in my logo
trajan bold
Professional
Nell Whitcombe
President
I do not want address on the card
nwhitcombe@rtballister-example.com
www.rtballister-example.com
CFO Advisory / Bookkeeping Plinwor Ledgerly Consulting
either logo without text or logo with text whichever is not used on the front of card.
rtballister rtballister
You can use other fonts, I just listed the one that is used in the text with the logo so you would know what that is. Pantone Hex Colors used: BLUE #012377 (C:96 - M:77 - Y:14 - K:4) #021856 (C:96 - M:82 - Y:28 - K:16) #095CD3 (C:95 - M:47 - Y:0 - K:0) Gold #987412 (C:29 - M:37 - Y:91 - K:16) #E4BB2C (C:9 - M:23 - Y:82 - K:1)

```html
<!DOCTYPE html>
<html lang="en">
<head>
<meta charset="utf-8">
<title>R.T. Ballister Holdings, LLC — Business Card</title>
<link rel="stylesheet" href="https://fonts.googleapis.com/css2?family=Cinzel:wght@400;700&display=swap">
<style>
  :root {
    --blue: #012377;
    --blue-deep: #021856;
    --blue-bright: #095CD3;
    --gold: #987412;
    --gold-light: #E4BB2C;
    --paper: #ffffff;
    --paper-tint: #f3f2ee;
    --backdrop: #e9e7e2;
    --ink-soft: #5a6180;
  }
  * { box-sizing: border-box; margin: 0; padding: 0; }
  html, body { width: 1200px; height: 891px; overflow: hidden; }
  body {
    background: var(--backdrop);
    font-family: "Cinzel", "Trajan Pro", serif;
    position: relative;
  }
  .card {
    position: absolute;
    top: 297px;
    width: 520px;
    height: 297px;
    background: var(--paper);
    box-shadow: 0 6px 22px rgba(0,0,0,0.14);
    overflow: hidden;
  }
  .card--front { left: 50px; }
  .card--back { left: 630px; }

  /* Front */
  .card-band { position: absolute; inset: 0; width: 100%; height: 100%; }
  .holder { position: absolute; left: 40px; top: 34px; }
  .holder-name {
    font-weight: 700; font-size: 29px; letter-spacing: 1px;
    color: var(--blue); text-transform: uppercase;
  }
  .holder-title {
    font-weight: 700; font-size: 17px; letter-spacing: 2px;
    color: var(--gold); text-transform: uppercase; margin-top: 2px;
    padding-bottom: 6px; border-bottom: 2px solid var(--gold-light);
    display: inline-block; padding-right: 60px;
  }
  .services {
    position: absolute; left: 40px; right: 24px; top: 128px;
    display: flex; gap: 26px; list-style: none;
  }
  .service {
    font-size: 10.5px; font-weight: 700; color: var(--blue);
    text-transform: uppercase; display: flex; align-items: center; gap: 5px;
  }
  .phones {
    position: absolute; left: 40px; right: 24px; top: 168px;
    display: flex; gap: 44px; list-style: none;
  }
  .contact {
    font-size: 10.5px; font-weight: 700; color: var(--blue);
    display: flex; align-items: center; gap: 6px;
  }
  .online {
    position: absolute; left: 40px; right: 24px; top: 248px;
    display: flex; gap: 36px; list-style: none;
  }
  .online .contact { color: var(--paper); font-size: 10px; }
  .icon { width: 12px; height: 12px; flex: none; }

  /* Back */
  .back-texture {
    position: absolute; inset: 0;
    background: linear-gradient(135deg, var(--paper) 0%, var(--paper-tint) 100%);
  }
  .brand {
    position: absolute; left: 0; right: 0; top: 124px;
    display: flex; align-items: center; justify-content: center; gap: 14px;
  }
  .brand-square { width: 42px; height: 42px; background: var(--blue); flex: none; }
  .brand-name {
    font-weight: 700; font-size: 24px; color: var(--blue); letter-spacing: 1px;
  }
</style>
</head>
<body>

<section class="card card--front" aria-label="Business card front">
  <svg class="card-band" viewBox="0 0 520 297" preserveAspectRatio="none" aria-hidden="true">
    <defs>
      <linearGradient id="bandFill" x1="0" y1="0" x2="1" y2="0">
        <stop offset="0" stop-color="var(--blue-deep)"/>
        <stop offset="0.6" stop-color="var(--blue)"/>
        <stop offset="1" stop-color="var(--blue-bright)"/>
      </linearGradient>
    </defs>
    <polygon points="0,212 520,200 520,210 0,222" fill="var(--gold-light)"/>
    <polygon points="0,226 520,214 520,297 0,297" fill="url(#bandFill)"/>
  </svg>

  <div class="holder">
    <h1 class="holder-name">Nell Whitcombe</h1>
    <p class="holder-title">President</p>
  </div>

  <ul class="services">
    <li class="service"><svg class="icon" viewBox="0 0 12 12"><path d="M1 6.5 L4.5 10 L11 2" fill="none" stroke="var(--gold-light)" stroke-width="2"/></svg>CFO Advisory</li>
    <li class="service"><svg class="icon" viewBox="0 0 12 12"><path d="M1 6.5 L4.5 10 L11 2" fill="none" stroke="var(--gold-light)" stroke-width="2"/></svg>Bookkeeping</li>
    <li class="service"><svg class="icon" viewBox="0 0 12 12"><path d="M1 6.5 L4.5 10 L11 2" fill="none" stroke="var(--gold-light)" stroke-width="2"/></svg>Plinwor Ledgerly Consulting</li>
  </ul>

  <ul class="phones">
    <li class="contact"><svg class="icon" viewBox="0 0 12 12"><circle cx="6" cy="6" r="6" fill="var(--blue)"/><path d="M4 3 L5 3 L5.5 4.8 L4.8 5.4 Q5.6 6.8 6.6 7.2 L7.2 6.5 L9 7 L9 8 Q8 9.2 6 8.2 Q3.8 7 3 4.6 Q3 3.4 4 3Z" fill="var(--paper)"/></svg>555.014.2036</li>
    <li class="contact"><svg class="icon" viewBox="0 0 12 12"><circle cx="6" cy="6" r="6" fill="var(--blue)"/><path d="M4 3 L5 3 L5.5 4.8 L4.8 5.4 Q5.6 6.8 6.6 7.2 L7.2 6.5 L9 7 L9 8 Q8 9.2 6 8.2 Q3.8 7 3 4.6 Q3 3.4 4 3Z" fill="var(--paper)"/></svg>555.019.4471</li>
    <li class="contact"><svg class="icon" viewBox="0 0 12 12"><circle cx="6" cy="6" r="6" fill="var(--blue)"/><path d="M4 3 L5 3 L5.5 4.8 L4.8 5.4 Q5.6 6.8 6.6 7.2 L7.2 6.5 L9 7 L9 8 Q8 9.2 6 8.2 Q3.8 7 3 4.6 Q3 3.4 4 3Z" fill="var(--paper)"/></svg>555.017.8352</li>
  </ul>

  <ul class="online">
    <li class="contact"><svg class="icon" viewBox="0 0 12 12"><circle cx="6" cy="6" r="5.4" fill="none" stroke="var(--paper)" stroke-width="1.2"/><rect x="3" y="4" width="6" height="4" fill="none" stroke="var(--paper)" stroke-width="0.9"/><path d="M3 4 L6 6.3 L9 4" fill="none" stroke="var(--paper)" stroke-width="0.9"/></svg>nwhitcombe@rtballister-example.com</li>
    <li class="contact"><svg class="icon" viewBox="0 0 12 12"><circle cx="6" cy="6" r="5.4" fill="none" stroke="var(--paper)" stroke-width="1.2"/><ellipse cx="6" cy="6" rx="2.2" ry="4" fill="none" stroke="var(--paper)" stroke-width="0.9"/><path d="M1.5 6 H10.5" stroke="var(--paper)" stroke-width="0.9"/></svg>www.rtballister-example.com</li>
  </ul>
</section>

<section class="card card--back" aria-label="Business card back">
  <div class="back-texture" role="img" aria-label="Subtle light textured paper pattern"></div>
  <div class="brand">
    <span class="brand-square" aria-hidden="true"></span>
    <span class="brand-name">R.T. BALLISTER HOLDINGS, LLC</span>
  </div>
</section>

</body>
</html>
```